Flyer for American Indian Elders on Dementia Warning Signs

We need a flyer designed for older adults who are American Indian or Alaska Native (in the U.S.).

Ideally, the flyer should complement the colors of our logos. The project logo and our organization logo are attached to the brief.

When people see the flyer we want them to feel that it represents their culture, is warm, and professional but relatable to older adults and people who have limited incomes.

I have attached an earlier draft of the document we designed ourselves BUT we want different and better.

It is for older adults who have trouble reading so:
1. you must use a font that is 11.5 points or larger
2. Do not put text over complex pictures or use shading with words
3. You can use a serif font for the heading, but should use san serif for the body text
4. There should be good contrast between the font color and background

Please do not use any images that include a head dress or pictures of American Indian people or things that are very traditional or "token" imagery.

We need to save a small space under the call out box/ somewhere on the flyer for other people to add their logo once they download.

Let us know if you have questions or need additional information.

Target Market(s)

Older American Indian people

Font styles to use
Serif
Sans Serif

Requirements
Must have
• Easy to read for older adults
Should not have
• indian headdress

```html
<!DOCTYPE html>
<html lang="en">
<head>
<meta charset="utf-8">
<title>10 Signs of Thinking or Memory Changes</title>
<link rel="stylesheet" href="https://fonts.googleapis.com/css2?family=Marcellus&family=Source+Sans+3:wght@400;600;700&display=swap">
<style>
:root{
  --page:#ece8e1;
  --paper:#fbfaf6;
  --clay:#8f4a40;
  --clay-text:#8a3f35;
  --teal:#2e8587;
  --teal-light:#8cc6c4;
  --ink:#2a2a2a;
  --white:#ffffff;
  --pattern-a:#c9dcd9;
  --pattern-b:#b86a5c;
}
*{box-sizing:border-box;margin:0;padding:0}
html,body{width:1200px;height:941px;overflow:hidden;background:var(--page)}
body{font-family:"Source Sans 3",sans-serif;color:var(--ink)}
.flyer{position:absolute;left:253px;top:20px;width:694px;height:900px;background:var(--paper);box-shadow:0 2px 10px rgba(0,0,0,.12);display:flex}
.main{position:relative;width:488px;height:100%}
.title-band{height:95px;background:var(--clay);padding:22px 22px 0 22px}
.title{font-family:"Marcellus",serif;color:var(--white);font-size:23.5px;line-height:33px;letter-spacing:.8px;font-weight:400}
.pattern-strip{height:18px;margin-top:4px;background:repeating-linear-gradient(90deg,var(--pattern-a) 0 9px,var(--pattern-b) 9px 12px)}
.intro{position:absolute;left:22px;right:22px;top:131px;font-size:12.2px;line-height:14.6px}
.intro strong{font-weight:700}
.signs{position:absolute;left:22px;right:18px;top:235px;height:632px;list-style:none;display:flex;flex-direction:column;justify-content:space-between}
.sign{display:flex;gap:9px}
.sign-num{flex:0 0 25px;height:25px;border-radius:50%;background:var(--clay);color:var(--white);font-weight:700;font-size:13px;display:flex;align-items:center;justify-content:center;margin-top:1px}
.sign-body{font-size:12.2px;line-height:14.8px;color:var(--clay-text)}
.sign-title{font-weight:700}
.sign-body ul{list-style:none;color:var(--ink);font-size:11.6px;line-height:15.4px}
.sign-body li::before{content:"• ";}
.footer-band{position:absolute;left:0;right:0;bottom:0;height:26px;background:var(--clay);color:var(--white);font-size:6.6px;line-height:8px;padding:4px 22px}
.side{position:relative;width:206px;height:100%}
.side-bg{position:absolute;inset:0}
.side-content{position:absolute;inset:0;text-align:center;color:var(--white)}
.org-name{position:absolute;top:60px;left:18px;right:18px;font-family:"Source Sans 3",sans-serif;font-weight:700;font-size:13px;line-height:15px;color:var(--white);text-transform:uppercase;letter-spacing:.6px}
.points-heading{position:absolute;top:178px;left:0;right:0;font-family:"Marcellus",serif;font-size:23px;letter-spacing:.6px}
.point{position:absolute;left:18px;right:18px;font-size:14px;line-height:17.6px}
.leaf{position:absolute;left:93px;width:20px;height:10px;border-radius:50%;background:var(--teal-light)}
.partner{position:absolute;top:738px;left:14px;right:10px;display:flex;align-items:center;gap:7px}
.partner-mark{width:36px;height:36px;border-radius:50%;border:2px solid var(--teal);flex:0 0 36px}
.partner-name{font-weight:600;font-size:13px;line-height:14px;color:var(--teal);text-align:left}
.learn{position:absolute;top:792px;left:14px;right:14px;font-size:10px;line-height:12.4px;color:var(--ink);text-align:center}
.links{position:absolute;top:840px;left:16px;list-style:none;font-size:11px;line-height:16px;font-weight:700;color:#3c3c3c}
.links li{display:flex;align-items:center;gap:5px}
</style>
</head>
<body>
<article class="flyer">
  <section class="main">
    <header class="title-band">
      <h1 class="title">10 SIGNS OF THINKING OR MEMORY CHANGES THAT MIGHT BE DEMENTIA</h1>
    </header>
    <div class="pattern-strip" role="img" aria-label="Woven zigzag border pattern in teal and clay"></div>
    <p class="intro">As we get older, we may slow down a bit. This is a normal part of aging. Changes in memory or thinking that make it harder to get through the day, are not a normal part of aging. These may be early signs of dementia. Because American Indian and Alaska Native people have a high risk of dementia, it is important to know the warning signs. <strong>Do you have any of these 10 signs? If so, talk to your doctor.</strong></p>
    <ol class="signs">
      <li class="sign"><span class="sign-num">1</span><div class="sign-body"><span class="sign-title">Memory loss that affects your daily life.</span> You may:<ul><li>Forget events or important dates</li><li>Repeat yourself</li><li>Rely more often on lists or sticky notes to remember things more often</li></ul></div></li>
      <li class="sign"><span class="sign-num">2</span><div class="sign-body"><span class="sign-title">Trouble planning or solving problems.</span> You may have a harder time:<ul><li>Paying bills</li><li>Cooking recipes you have used for years</li></ul></div></li>
      <li class="sign"><span class="sign-num">3</span><div class="sign-body"><span class="sign-title">Get confused about the time, date, or where you are.</span></div></li>
      <li class="sign"><span class="sign-num">4</span><div class="sign-body"><span class="sign-title">Daily tasks are getting harder,</span> including:<ul><li>Driving</li><li>Making a grocery list or going shopping</li></ul></div></li>
      <li class="sign"><span class="sign-num">5</span><div class="sign-body"><span class="sign-title">Trouble with how your eyesight and thinking work together that gets worse.</span> This includes:<ul><li>Tripping, falls, or problems with your balance</li><li>Spilling or dropping things more</li></ul></div></li>
      <li class="sign"><span class="sign-num">6</span><div class="sign-body"><span class="sign-title">New trouble talking or writing.</span> You have a hard time finding the words you want to say. For example, you may say “that thing on your wrist that tells time” instead of “watch.”</div></li>
      <li class="sign"><span class="sign-num">7</span><div class="sign-body"><span class="sign-title">Lose and cannot find things.</span> For example, you:<ul><li>Can’t find the coffee pot that you use every day</li><li>Might put your car keys in the freezer</li></ul></div></li>
      <li class="sign"><span class="sign-num">8</span><div class="sign-body"><span class="sign-title">Notice changes in mood or personality,</span> such as being:<ul><li>Easily mad or sad in everyday situations</li><li>More fearful (scared) or suspicious (not trusting)</li></ul></div></li>
      <li class="sign"><span class="sign-num">9</span><div class="sign-body"><span class="sign-title">Act different and make poor choices.</span> This may make you more likely to:<ul><li>Spend money you do not have or be a scam victim</li><li>Stop washing up regularly or pay less attention to how you look</li><li>Forget to take care of your pet</li></ul></div></li>
      <li class="sign"><span class="sign-num">10</span><div class="sign-body"><span class="sign-title">Pull away from friends and family because it is harder to keep up.</span> You may not want to do things you used to enjoy, like sporting events, church, music, or sex.</div></li>
    </ol>
    <footer class="footer-band">Adapted from resources from the Memory Health Alliance &amp; Plains State University. PSU materials created in collaboration with regional tribal members. Funding support provided by the National Healthy Aging Office.</footer>
  </section>
  <aside class="side">
    <svg class="side-bg" width="206" height="900" viewBox="0 0 206 900" aria-hidden="true">
      <polygon points="0,0 206,0 206,718 0,676" fill="var(--teal)"/>
      <polygon points="0,676 206,718 206,726 0,684" fill="#d9ebe9"/>
    </svg>
    <div class="side-content">
      <p class="org-name">Native Elders Wellness Alliance</p>
      <h2 class="points-heading">MAIN POINTS</h2>
      <p class="point" style="top:225px">American Indian and Alaska Native people have a high risk of dementia.</p>
      <span class="leaf" style="top:310px" role="img" aria-label="Small leaf ornament"></span>
      <p class="point" style="top:339px">Big changes in memory or thinking that make it hard to get through the day are not a normal part of aging.</p>
      <span class="leaf" style="top:442px" role="img" aria-label="Small leaf ornament"></span>
      <p class="point" style="top:469px">People with one or more of these 10 signs should talk to their doctor to find the cause. It is not always dementia.</p>
      <span class="leaf" style="top:573px" role="img" aria-label="Small leaf ornament"></span>
      <p class="point" style="top:601px">Early dementia diagnosis gives you a chance to get care and plan your future.</p>
      <div class="partner">
        <span class="partner-mark"></span>
        <span class="partner-name">Elder Brain Health Circle</span>
      </div>
      <p class="learn">To learn more about the warning signs of dementia in American Indian and Alaska Native people, visit:</p>
      <ul class="links">
        <li><svg width="9" height="9" viewBox="0 0 10 10" aria-hidden="true"><circle cx="5" cy="5" r="4.2" fill="none" stroke="var(--teal)" stroke-width="1.2"/><path d="M1 5h8M5 1c-2 2.5-2 5.5 0 8M5 1c2 2.5 2 5.5 0 8" fill="none" stroke="var(--teal)" stroke-width=".9"/></svg>www.elderbraincircle.org</li>
        <li><svg width="9" height="9" viewBox="0 0 10 10" aria-hidden="true"><circle cx="5" cy="5" r="4.2" fill="none" stroke="var(--teal)" stroke-width="1.2"/><path d="M1 5h8M5 1c-2 2.5-2 5.5 0 8M5 1c2 2.5 2 5.5 0 8" fill="none" stroke="var(--teal)" stroke-width=".9"/></svg>www.healthyagingoffice.org</li>
      </ul>
    </div>
  </aside>
</article>
</body>
</html>
```